Salve Label

2.25 inch round label.

We are looking for a simple label, muted natural colors, sophisticated, elegant, calming.

Name of Product: Herbal Beeswax Salve
This scent is lavender - but there will be others scents
Want this label to be adaptable to other scents with simple color and word changes.

Other things to express on the label - all natural, calming, relaxing

Name of the Company: Tansy Ridge Farm
2 oz.

```html
<!DOCTYPE html>
<html lang="en">
<head>
<meta charset="utf-8">
<title>Lavender Herbal Beeswax Salve Label</title>
<link rel="stylesheet" href="https://fonts.googleapis.com/css2?family=Cinzel:wght@400;500&display=swap">
<style>
  :root {
    --backdrop: #e4e0dc;
    --scent-band: #c9c9e0;
    --label-cream: #f1f0e9;
    --ink: #141414;
  }
  html, body {
    margin: 0;
    padding: 0;
    width: 1200px;
    height: 831px;
    overflow: hidden;
    background: var(--backdrop);
  }
  .salve-label {
    display: block;
    width: 1200px;
    height: 831px;
    font-family: "Cinzel", "Times New Roman", serif;
  }
  .scent-band { fill: var(--scent-band); }
  .label-center { fill: var(--label-cream); stroke: var(--ink); stroke-width: 3; }
  .scent-name { fill: var(--ink); font-size: 74px; letter-spacing: 4px; }
  .benefit-line { fill: var(--ink); font-size: 44px; letter-spacing: 3px; }
  .farm-name { fill: var(--ink); font-size: 40px; font-weight: 500; letter-spacing: 2px; }
  .product-name { fill: var(--ink); font-size: 44px; font-weight: 500; }
  .net-weight { fill: var(--ink); font-size: 30px; }
</style>
</head>
<body>
<svg class="salve-label" viewBox="0 0 1200 831" xmlns="http://www.w3.org/2000/svg">
  <defs>
    <path id="top-arc" d="M 600 750 A 335 335 0 0 1 600 80 A 335 335 0 0 1 600 750"/>
    <path id="bottom-arc" d="M 600 52 A 363 363 0 0 0 600 778 A 363 363 0 0 0 600 52"/>
  </defs>

  <circle class="scent-band" cx="600" cy="415" r="392"/>
  <circle class="label-center" cx="600" cy="415" r="288"/>

  <text class="scent-name" text-anchor="middle">
    <textPath href="#top-arc" startOffset="50%">LAVENDER</textPath>
  </text>

  <text class="benefit-line" text-anchor="middle">
    <textPath href="#bottom-arc" startOffset="50%">AllNatural  •●•  Calming  •●•  Relaxing</textPath>
  </text>

  <text class="farm-name" x="600" y="345" text-anchor="middle">Tansy Ridge Farm</text>

  <text class="product-name" x="600" y="480" text-anchor="middle">Herbal Beeswax</text>
  <text class="product-name" x="600" y="530" text-anchor="middle">Salve</text>

  <text class="net-weight" x="600" y="610" text-anchor="middle">2 oz.(56.7g)</text>
</svg>
</body>
</html>
```